Northgate Baptist Church Banner Design

Designing 6 banners (3 + 3 that will hang on opposite sides of our auditorium) that are 10 feet long by 4 feet wide.

Use our branding guide - specifically item 4 (vertical logo) and item 5 (icon logo).

Design elements found in our ASCEND booklet, we would like to see designs that utilize the white, green and blue colour palettes but NOT the grey. Other colours may be incorporated (e.g. coral).

We are looking for 3 banner designs that would match on either side of the auditorium, the first banner incorporating the word "TRUTH", the second incorporating the word "LOVE", and the third incorporating the word "MISSION".

We interested in incorporating graphics such as trees or outdoor themes.

Font styles to use
Other font styles liked:
• Montserrat

Colors
34a7d7
00a990
f47c35

Requirements
Must have
• Banner Type #1 include the word "TRUTH"
Banner Type #2 include the word "LOVE"
Banner Type #3 include the word "MISSION"

Colour scheme must include CMYK 54 / 5 / 16 / 0 (which is available in the branding guide.) We have selected the three colours, included below in the brief.

From the branding guide - utilize #5 (icon) for the banner.

UPDATE: After reviewing the initial submissions, we are asking for designs that ONLY incorporate #5 - the ICON logo for the banners.
Nice to have
• It would be nice to have some creativity with the colour ... though a more minimalistic style is preferred.

Graphic adaptations such as trees in the background would be of interest.
Should not have
• Colour scheme should not be gray scale.

The banners should NOT be too busy.

Scripture verses (written out) are not necessary.

```html
<!DOCTYPE html>
<html lang="en">
<head>
<meta charset="utf-8">
<title>Love Never Fails Banner</title>
<link rel="stylesheet" href="https://fonts.googleapis.com/css2?family=Montserrat:wght@600;700&family=Kaushan+Script&family=Cormorant+Garamond:ital,wght@1,500&display=swap">
<style>
  :root {
    --banner-teal: #0f7c93;
    --accent-coral: #f47c35;
    --text-white: #ffffff;
    --mark-tint: #8fd0e0;
  }
  html, body {
    margin: 0;
    padding: 0;
    width: 1200px;
    height: 2796px;
    overflow: hidden;
    background: var(--banner-teal);
  }
  .banner {
    position: relative;
    width: 1200px;
    height: 2796px;
    background: var(--banner-teal);
    overflow: hidden;
  }
  .headline {
    position: absolute;
    left: 0;
    top: 0;
    width: 100%;
    height: 100%;
    margin: 0;
    font-weight: normal;
  }
  .headline-word {
    position: absolute;
    display: block;
    white-space: nowrap;
    line-height: 1;
  }
  .headline-love {
    left: 176px;
    top: 650px;
    font-family: "Montserrat", sans-serif;
    font-weight: 700;
    font-size: 336px;
    letter-spacing: -8px;
    color: var(--text-white);
  }
  .headline-fails {
    left: 228px;
    top: 1117px;
    font-family: "Montserrat", sans-serif;
    font-weight: 700;
    font-size: 380px;
    letter-spacing: -6px;
    color: var(--text-white);
  }
  .headline-never {
    left: 190px;
    top: 870px;
    font-family: "Kaushan Script", cursive;
    font-weight: 400;
    font-size: 270px;
    color: var(--accent-coral);
    transform: rotate(-4deg);
    transform-origin: left center;
    z-index: 2;
  }
  .verse-reference {
    position: absolute;
    left: 0;
    top: 1510px;
    width: 100%;
    margin: 0;
    text-align: center;
    font-family: "Cormorant Garamond", serif;
    font-style: italic;
    font-weight: 500;
    font-size: 110px;
    line-height: 1;
    color: var(--text-white);
  }
  .church-mark {
    position: absolute;
    left: 70px;
    bottom: 170px;
    margin: 0;
    font-family: "Montserrat", sans-serif;
    font-weight: 600;
    font-size: 96px;
    line-height: 1;
    color: var(--mark-tint);
  }
</style>
</head>
<body>
  <main class="banner">
    <h1 class="headline">
      <span class="headline-word headline-love">Love</span>
      <span class="headline-word headline-fails">fails</span>
      <span class="headline-word headline-never">never</span>
    </h1>
    <p class="verse-reference">1 Corinthians 13:8</p>
    <p class="church-mark">Ridgeway</p>
  </main>
</body>
</html>
```